- Redesign our business card
- Logo remains unchanged
- Current business card attached

Target Market(s)

We are a property management company

Industry/Entity Type

Business

```html
<!DOCTYPE html>
<html lang="en">
<head>
<meta charset="utf-8">
<title>Harlow Property Group – Business Card</title>
<link href="https://fonts.googleapis.com/css2?family=Open+Sans:wght@400;600;700&family=Cinzel&display=swap" rel="stylesheet">
<style>
  :root {
    --bg: #d3d3d3;
    --card-front-frame: #e4e3da;
    --card-back-frame: #a9a9a9;
    --panel: #fbfbfa;
    --panel-shade: #ecebe8;
    --olive: #7f7f2a;
    --sand: #e8dfb8;
    --slate: #656566;
    --ink: #5a5a5a;
    --ink-soft: #777;
    --label: #333;
  }
  * { margin: 0; padding: 0; box-sizing: border-box; }
  html, body { width: 1200px; height: 895px; overflow: hidden; }
  body {
    background: var(--bg);
    font-family: "Open Sans", Arial, sans-serif;
    position: relative;
  }
  .card {
    position: absolute;
    top: 302px;
    width: 570px;
    height: 343px;
    border-radius: 16px;
  }
  .card--front { left: 18px; background: var(--card-front-frame); }
  .card--back { left: 612px; background: linear-gradient(90deg, #9c9c9c, #bdbdbd 50%, #9c9c9c); }
  .card__panel {
    position: absolute;
    left: 29px; top: 21px;
    width: 513px; height: 295px;
    border-radius: 18px;
    background: radial-gradient(ellipse at 55% 25%, #ffffff 0%, var(--panel) 55%, var(--panel-shade) 100%);
  }
  .brand { position: absolute; display: flex; align-items: center; }
  .brand__square { background: var(--olive); flex: none; }
  .brand__name { font-weight: 700; color: var(--slate); white-space: nowrap; }
  .brand--front { left: 67px; top: 105px; gap: 14px; }
  .brand--front .brand__square { width: 58px; height: 58px; }
  .brand--front .brand__name { font-size: 17px; letter-spacing: 0.2px; }
  .brand__tagline {
    position: absolute; left: 67px; top: 174px;
    font-size: 12px; color: var(--slate); letter-spacing: 0.4px;
  }
  .brand--back { left: 33px; top: 26px; gap: 6px; }
  .brand--back .brand__square { width: 22px; height: 22px; opacity: 0.7; }
  .brand--back .brand__name { font-size: 8px; color: #9a9a9a; }
  .holder {
    position: absolute; right: 283px; top: 105px; text-align: right;
  }
  .holder__name { font-size: 17px; font-weight: 600; color: var(--ink); letter-spacing: 0.2px; line-height: 1.1; }
  .holder__title { font-size: 6.5px; font-weight: 700; color: var(--olive); letter-spacing: 0.3px; margin-top: 3px; }
  .divider {
    position: absolute; left: 244px; top: 90px;
    width: 1.5px; height: 93px; background: var(--ink);
  }
  .contact {
    position: absolute; left: 258px; top: 105px;
    font-size: 9.6px; line-height: 12px; color: var(--ink);
    list-style: none; white-space: nowrap;
  }
  .contact strong { font-weight: 700; }
  .services {
    position: absolute; left: 0; right: 0; top: 230px;
    text-align: center; font-size: 8.3px; font-weight: 600;
    letter-spacing: 1.6px; color: var(--olive); white-space: nowrap;
  }
  .face-label {
    position: absolute; top: 686px;
    font-family: "Cinzel", Georgia, serif; font-size: 15px;
    letter-spacing: 3px; color: var(--label);
  }
  .face-label--front { left: 66px; }
  .face-label--back { left: 660px; }
</style>
</head>
<body>
  <section class="card card--front" aria-label="Card front">
    <div class="card__panel">
      <div class="brand brand--front">
        <span class="brand__square"></span>
        <span class="brand__name">HARLOW PROPERTY GROUP</span>
      </div>
      <p class="brand__tagline">STRATA MANAGEMENT SERVICES</p>
    </div>
  </section>

  <section class="card card--back" aria-label="Card back">
    <div class="card__panel">
      <div class="brand brand--back">
        <span class="brand__square"></span>
        <span class="brand__name">HARLOW PROPERTY GROUP</span>
      </div>
      <div class="holder">
        <p class="holder__name">DANIEL HARLOW</p>
        <p class="holder__title">LICENSED STRATA MANAGER</p>
      </div>
      <span class="divider"></span>
      <ul class="contact">
        <li>PO BOX 48, ELMWOOD BAY NSW 2031</li>
        <li>12/6-18 LINDEN STREET ELMWOOD NSW 2030</li>
        <li>T: <strong>02 9000 1470</strong></li>
        <li>F: <strong>02 9000 1480</strong></li>
        <li>M: <strong>0400 555 182</strong></li>
        <li>E: info@harlowproperty.example</li>
        <li>www.harlowproperty.example</li>
      </ul>
      <p class="services">STRATA MANAGEMENT | COMMUNITY MANAGEMENT | PROPERTY MANAGEMENT</p>
    </div>
  </section>

  <p class="face-label face-label--front">FRONT</p>
  <p class="face-label face-label--back">BACK</p>
</body>
</html>
```